Pilates Classes Flyer Design

I need a flyer designed that will promote my range of classes held in Bath, UK. I teach beginners, intermediate level and Over 50's and 60's and also teach individuals in their own homes. I would like to see designs using my colours blue Pantone 306 and Lime Green 14-0452 TPX TCX. The flyer should reflect a friendly, welcoming and professional class structure. I attach an old flyer for your reference and copy.

Target Market(s)

Men and Women who have busy lives working hard, who recognise they need to stretch out, do some exercise and de-stress after a busy day

Ladies over 50 who want to do some Pilates in a friendly fun environment and meet people at the same time.

Industry/Entity Type

It Professional

Font styles to use
Sans Serif
Script

Requirements
Must have
• One-sided flyer
Text only logo. Drop the figure

```html
<!DOCTYPE html>
<html lang="en">
<head>
<meta charset="utf-8">
<title>Pilates Classes Flyer</title>
<link rel="stylesheet" href="https://fonts.googleapis.com/css2?family=Arimo:wght@400;700&family=Parisienne&display=swap">
<style>
  :root {
    --brand-blue: #12a9e1;
    --brand-green: #76a33a;
    --text-grey: #6b6b6b;
    --text-dark: #2e2e2e;
    --page-bg: #e9e9e7;
    --flyer-top: #ffffff;
    --flyer-bottom: #eeeeee;
    --decor-tint: #dcecf6;
  }
  * { margin: 0; padding: 0; box-sizing: border-box; }
  html, body {
    width: 1200px; height: 1065px; overflow: hidden;
    background: var(--page-bg);
    font-family: "Arimo", Arial, sans-serif;
  }
  .flyer {
    position: absolute; left: 250px; top: 40px;
    width: 699px; height: 985px;
    background: linear-gradient(160deg, var(--flyer-top) 0%, var(--flyer-top) 45%, var(--flyer-bottom) 100%);
    overflow: hidden;
    text-align: center;
  }
  .decor {
    position: absolute; border-radius: 50%;
    background: radial-gradient(circle, var(--decor-tint) 0%, rgba(220,236,246,0) 70%);
    opacity: .8;
  }
  .decor--top { left: -60px; top: -40px; width: 420px; height: 320px; }
  .decor--bottom { left: -80px; top: 700px; width: 440px; height: 340px; }
  .line { position: absolute; left: 0; width: 100%; white-space: nowrap; }
  .title {
    top: 18px; font-family: "Parisienne", cursive; font-size: 150px;
    line-height: 150px; color: var(--brand-blue);
  }
  .swoosh { position: absolute; left: 110px; top: 140px; width: 480px; height: 50px; }
  .headline { top: 198px; font-size: 33px; line-height: 36px; color: var(--brand-green); }
  .intro {
    top: 256px; font-size: 26px; line-height: 33.5px; color: var(--text-grey);
  }
  .features { top: 372px; font-size: 17px; line-height: 26.5px; color: var(--text-grey); }
  .features .strong { color: var(--text-dark); }
  .join { top: 497px; font-size: 19px; line-height: 24px; color: var(--text-dark); }
  .venues { top: 524px; font-size: 18px; line-height: 25px; color: var(--text-dark); }
  .venue-name { color: var(--brand-blue); }
  .contact {
    top: 680px; font-size: 35px; line-height: 43px; font-weight: 700;
    color: var(--brand-green); letter-spacing: .3px;
  }
  .brand-box {
    position: absolute; left: 214px; top: 772px; width: 277px; height: 188px;
    background: #fff;
    display: flex; flex-direction: column; align-items: center; justify-content: center;
    color: var(--brand-blue); font-size: 34px; line-height: 40px;
  }
  .brand-box .sub { font-size: 20px; letter-spacing: 4px; line-height: 28px; }
</style>
</head>
<body>
  <main class="flyer">
    <div class="decor decor--top" role="img" aria-label="Faint floral pattern"></div>
    <div class="decor decor--bottom" role="img" aria-label="Faint floral pattern"></div>

    <h1 class="line title">Pilates</h1>
    <svg class="swoosh" viewBox="0 0 480 50" aria-hidden="true">
      <path d="M2 46 C 120 8, 330 -2, 478 10 C 330 8, 140 20, 2 46 Z" fill="var(--brand-blue)"/>
    </svg>

    <p class="line headline">New classes near you!</p>

    <p class="line intro">Pilates is for EVERYONE whatever level<br>of fitness, age or ability to help you build<br>strength, flexibility and overall well-being.</p>

    <p class="line features">
      <span class="strong">Quality teaching with Certified Mat Method Teacher.</span><br>
      Progressive approach. Teaching good movement skills.<br>
      <span class="strong">Small class sizes and friendly atmosphere.</span><br>
      Beginners, Intermediate and Over 50's classes to choose from.
    </p>

    <p class="line join">Join my one-hour classes at:</p>
    <p class="line venues">
      <span class="venue-name">St Aidan's Church Hall, Elm Rise</span><br>
      Monday evenings, Tuesday and Friday mornings.<br>
      <span class="venue-name">Brookfield Medical Centre</span><br>
      Tuesday evenings.<br>
      <span class="venue-name">Ashcombe Centre, Mill Road,</span><br>
      Wednesday mornings and evenings.
    </p>

    <p class="line contact">Call Helen on 07700 900418<br>helen.marsh@example.co.uk</p>

    <div class="brand-box">
      <span>Centre Line</span>
      <span class="sub">PILATES</span>
    </div>
  </main>
</body>
</html>
```